Business Card Design Project

Hi,
This is a simple contest. The logo for the back of the card is deigned. See attached files. The front of the card must have :

Directors Name: Tobias
Mob:
e-mail:
Postal Address:
Web Page Adress:

It may also add words: "Leaders in Construction Project Management Services"

Target Market(s)

Business & Home owners alike

Industry/Entity Type

Business

Requirements
Must have
• See details above and logo attached
Should not have
• Images other than logo

```html
<!DOCTYPE html>
<html lang="en">
<head>
<meta charset="utf-8">
<title>Northbeam Projects – Business Card</title>
<link href="https://fonts.googleapis.com/css2?family=Arimo:wght@400;700&display=swap" rel="stylesheet">
<style>
  :root {
    --stage: #2a2a2a;
    --card-white: #ffffff;
    --brand-blue: #119ddb;
    --ink: #1a1a1a;
    --strip: #222323;
  }
  * { margin: 0; padding: 0; box-sizing: border-box; }
  html, body {
    width: 1200px; height: 1200px; overflow: hidden;
    background: var(--stage);
    font-family: "Arimo", Arial, sans-serif;
  }
  .card {
    position: absolute; left: 150px; width: 900px; height: 514px;
    overflow: hidden;
    box-shadow: 0 18px 40px rgba(0,0,0,0.45);
  }
  .card--front { top: 70px; background: var(--card-white); }
  .card--back { top: 624px; background: var(--brand-blue); }

  .brand { position: absolute; display: flex; align-items: center; gap: 18px; }
  .brand__square { width: 58px; height: 58px; }
  .brand__name {
    font-weight: 700; font-size: 46px; letter-spacing: 1px; line-height: 1;
    text-transform: uppercase;
  }
  .card--front .brand { left: 210px; top: 92px; }
  .card--front .brand__square { background: var(--brand-blue); }
  .card--front .brand__name { color: var(--brand-blue); }
  .card--back .brand { left: 50%; top: 50%; transform: translate(-50%, -50%); }
  .card--back .brand__square { background: var(--card-white); }
  .card--back .brand__name { color: var(--card-white); }

  .holder { position: absolute; left: 84px; top: 268px; }
  .holder__name { color: var(--brand-blue); font-size: 27px; }
  .holder__title { color: var(--ink); font-size: 24px; margin-top: 4px; }

  .contact { position: absolute; left: 486px; top: 210px; color: var(--ink); font-size: 19px; }
  .contact__address { line-height: 1.25; margin-bottom: 10px; }
  .contact__list { list-style: none; padding-left: 28px; }
  .contact__item { display: flex; align-items: center; gap: 12px; margin-bottom: 6px; }
  .contact__icon { width: 20px; height: 20px; flex: none; }

  .footer-band { position: absolute; left: 0; bottom: 0; width: 900px; height: 130px; }
  .footer-band__url {
    position: absolute; right: 60px; bottom: 28px;
    color: var(--card-white); font-size: 28px; letter-spacing: 0.5px;
  }
</style>
</head>
<body>

<section class="card card--front">
  <div class="brand">
    <span class="brand__square"></span>
    <span class="brand__name">Northbeam Projects</span>
  </div>

  <div class="holder">
    <p class="holder__name">Angelo Tobias</p>
    <p class="holder__title">Your Titel</p>
  </div>

  <div class="contact">
    <p class="contact__address">Your postal Address,Your postal<br>Address,Your postal Address</p>
    <ul class="contact__list">
      <li class="contact__item">
        <svg class="contact__icon" viewBox="0 0 20 20"><rect width="20" height="20" rx="4" fill="#119ddb"/><path d="M6 4.5l2.2 0 1 3-1.4 1.1a7 7 0 0 0 3.6 3.6l1.1-1.4 3 1 0 2.2c-5.2.6-10.1-4.3-9.5-9.5z" fill="#fff"/></svg>
        <span>00000000</span>
      </li>
      <li class="contact__item">
        <svg class="contact__icon" viewBox="0 0 20 20"><rect y="3" width="20" height="14" rx="2" fill="#119ddb"/><path d="M2 5l8 6 8-6" stroke="#fff" stroke-width="1.6" fill="none"/></svg>
        <span>angelo@northbeamprojects.com</span>
      </li>
      <li class="contact__item">
        <svg class="contact__icon" viewBox="0 0 20 20" fill="none" stroke="#119ddb" stroke-width="1.5"><circle cx="10" cy="10" r="8.5"/><ellipse cx="10" cy="10" rx="3.8" ry="8.5"/><path d="M1.5 10h17M3 5.5h14M3 14.5h14"/></svg>
        <span>www.northbeamprojects.com</span>
      </li>
    </ul>
  </div>

  <svg class="footer-band" viewBox="0 0 900 130" aria-hidden="true">
    <rect x="0" y="94" width="900" height="36" fill="#222323"/>
    <polygon points="430,130 438,58 850,58 900,84 900,130" fill="#119ddb"/>
  </svg>
  <p class="footer-band__url">www.northbeamprojects.com</p>
</section>

<section class="card card--back">
  <div class="brand">
    <span class="brand__square"></span>
    <span class="brand__name">Northbeam Projects</span>
  </div>
</section>

</body>
</html>
```